Home Design company focused on remodel and enhancement of kitchens and bathroorms

I already have a logo designed by ArtHarbor, I now need a design for my business cards.
The company is in the remodeling and enhancement industry for homes, focusing on kitchens and bathrooms, however, we can remodel or enhance every room in a home, an office space, etc.

The company's name is VELMOR HOME DESIGN, LLC

We'll focus on clients in the Rio Grande Valley, Texas. Primarily McAllen, Edinburg, Pharr, Mission, Brownsville and South Padre Island.

The design on the business card should transmit reliability, professionalism anda bit of upscale design.

The logo is in black and white, and would like to keep it that way.

The information that needs to be printed in the business cards is:
Company's name: Velmor Home Design
Company's Logo (attached)
My name: Noel Bramwit
Address, phone and email:
2715 N Parkline Road, Ste 348
McAllen, TX 78501
(956) 555 0187
nbramwit@velmordesign.example
Website: velmordesign.example

```html
<!DOCTYPE html>
<html lang="en">
<head>
<meta charset="utf-8">
<title>Velmor Home Design – Business Card</title>
<link rel="stylesheet" href="https://fonts.googleapis.com/css2?family=Arimo:wght@400;700&display=swap">
<style>
  :root {
    --page-bg: #121212;
    --card-bg: #1e1e1f;
    --card-edge: #2a2a2b;
    --ink: #f4f4f4;
    --rule: #e8e8e8;
    --mark-tone: rgba(255,255,255,.06);
  }
  * { box-sizing: border-box; margin: 0; padding: 0; }
  html, body {
    width: 1200px; height: 963px; overflow: hidden;
    background: var(--page-bg);
  }
  .sheet {
    width: 1200px; height: 963px;
    display: flex; flex-direction: column;
    align-items: center; justify-content: center; gap: 44px;
  }
  .card {
    position: relative;
    width: 700px; height: 400px;
    background: var(--card-bg);
    border: 1px solid var(--card-edge);
    box-shadow: 0 14px 30px rgba(0,0,0,.55);
    color: var(--ink);
    font-family: "Arimo", Arial, sans-serif;
    overflow: hidden;
  }
  .brand-mark-area {
    position: absolute;
    background: linear-gradient(135deg, var(--mark-tone), rgba(255,255,255,.02));
  }
  .brand-name {
    display: flex; align-items: center; gap: 10px;
    font-family: "Arimo", Arial, sans-serif;
    font-weight: 400;
    color: var(--ink);
    white-space: nowrap;
  }
  .brand-name .brand-square {
    width: 16px; height: 16px; background: var(--ink); flex: none;
  }
  /* front */
  .card-front .brand-mark-area {
    left: 330px; top: 0; width: 370px; height: 400px;
  }
  .card-front .brand-name {
    position: absolute; right: 48px; top: 64px;
    font-size: 22px;
  }
  .card-front .holder-name {
    position: absolute; left: 48px; top: 60px;
    font-size: 27px; font-weight: 700; letter-spacing: .02em;
    text-transform: uppercase;
  }
  .card-front .name-rule {
    position: absolute; left: 44px; top: 100px;
    width: 270px; height: 1.5px; background: var(--rule);
  }
  .card-front .divider {
    position: absolute; left: 44px; right: 44px; top: 188px;
    height: 1.5px; background: var(--rule);
  }
  .contact-list {
    position: absolute; left: 48px; top: 118px;
    list-style: none; font-size: 17px; line-height: 22px;
  }
  .contact-list li { display: flex; align-items: center; gap: 10px; }
  .contact-list svg { width: 14px; height: 14px; flex: none; }
  .address {
    position: absolute; right: 48px; top: 222px;
    font-style: normal; text-align: right;
    font-size: 20px; line-height: 26px;
  }
  /* back */
  .card-back .brand-name {
    position: absolute; left: 50%; top: 78px; transform: translateX(-50%);
    font-size: 30px;
  }
  .card-back .brand-mark-area {
    left: 90px; top: 170px; width: 520px; height: 230px;
    background: linear-gradient(160deg, rgba(255,255,255,.03), rgba(255,255,255,.12) 70%, rgba(255,255,255,.04));
  }
</style>
</head>
<body>
<main class="sheet">

  <section class="card card-front" aria-label="Business card front">
    <div class="brand-mark-area" role="img" aria-label="Large faint brand symbol watermark"></div>
    <h1 class="holder-name">Noel Bramwit</h1>
    <div class="name-rule"></div>
    <ul class="contact-list">
      <li>
        <svg viewBox="0 0 16 16" aria-hidden="true"><path d="M4 1.5l2.2 3-1.3 1.6c.8 1.9 2.1 3.3 4 4.2l1.6-1.3 3 2.2-1.2 2.6C7 13.6 2.4 9 1.5 2.7z" fill="none" stroke="currentColor" stroke-width="1.3"/></svg>
        <span>956-555 0187</span>
      </li>
      <li>
        <svg viewBox="0 0 16 16" aria-hidden="true"><rect x="1.5" y="3.5" width="13" height="9" fill="none" stroke="currentColor" stroke-width="1.2"/><path d="M1.5 3.5L8 9l6.5-5.5" fill="none" stroke="currentColor" stroke-width="1.2"/></svg>
        <span>nbramwit@velmordesign.example</span>
      </li>
      <li>
        <svg viewBox="0 0 16 16" aria-hidden="true"><circle cx="8" cy="8" r="6.5" fill="none" stroke="currentColor" stroke-width="1.2"/><ellipse cx="8" cy="8" rx="2.8" ry="6.5" fill="none" stroke="currentColor" stroke-width="1"/><path d="M1.5 8h13M2.5 5h11M2.5 11h11" stroke="currentColor" stroke-width="1"/></svg>
        <span>www.velmordesign.example</span>
      </li>
    </ul>
    <div class="brand-name"><span class="brand-square" aria-hidden="true"></span>Velmor Home Design</div>
    <div class="divider"></div>
    <address class="address">
      2715 N Parkline Road<br>
      Ste 348<br>
      McAllen, TX 78501
    </address>
  </section>

  <section class="card card-back" aria-label="Business card back">
    <div class="brand-name"><span class="brand-square" aria-hidden="true"></span>Velmor Home Design</div>
    <div class="brand-mark-area" role="img" aria-label="Large glossy brand symbol decoration"></div>
  </section>

</main>
</body>
</html>
```